R. Dalworth Billboard

2 miles ahead on right
Voted number 1 ... again!
California cuisine
Located in Historic Bramble Hollow Inn
Picture of a couple dining
www.marduvel.com 555.317.0962

Target Market(s)

travelers

Industry/Entity Type

hospitality

Font styles to use
Serif

Colors
59FF00
82FF00
B8FF75
E3FFCB
F4FFEA
EE7325
F08F49
F5BC92
FAE3D3
FDF4ED

Requirements
Should not have
• bright colors

```html
<!DOCTYPE html>
<html lang="en">
<head>
<meta charset="utf-8">
<title>R. Dalworth Billboard</title>
<link rel="stylesheet" href="https://fonts.googleapis.com/css2?family=Saira+Semi+Condensed:wght@600;700;800&family=Saira:wght@500;600;700&family=Bitter:wght@700&display=swap">
<style>
  :root {
    --board-dark: #1f130e;
    --headline-gold: #f1be12;
    --text-white: #ffffff;
    --panel-white: #ffffff;
    --panel-yellow: #f8c73a;
    --olive-green: #56761c;
    --brand-orange: #e4501f;
    --lime-dot: #a8d43c;
    --photo-deep: #3a1d0c;
    --photo-warm: #b65a1c;
    --photo-glow: #e88a3a;
  }
  * { margin: 0; padding: 0; box-sizing: border-box; }
  html, body {
    width: 1200px; height: 500px; overflow: hidden;
    background: var(--board-dark);
  }
  .billboard {
    position: relative; width: 1200px; height: 500px;
    background: var(--board-dark);
    font-family: "Saira Semi Condensed", "Saira", sans-serif;
    overflow: hidden;
  }
  .dining-photo {
    position: absolute; left: 0; top: 0; width: 559px; height: 500px;
    background:
      radial-gradient(ellipse at 70% 75%, var(--photo-glow) 0%, rgba(232,138,58,0) 55%),
      radial-gradient(ellipse at 40% 35%, var(--photo-warm) 0%, rgba(182,90,28,0) 60%),
      linear-gradient(160deg, var(--photo-deep) 0%, #6b3312 55%, #8a4417 100%);
  }
  .voted-badge {
    position: absolute; left: 26px; top: 300px;
    color: var(--text-white);
  }
  .voted-words {
    position: absolute; left: 0; top: 2px;
    font-family: "Saira", sans-serif; font-weight: 700;
    font-size: 50px; line-height: 60px; letter-spacing: -0.5px;
    white-space: nowrap;
  }
  .voted-number {
    position: absolute; left: 224px; top: -30px;
    font-family: "Bitter", serif; font-weight: 700;
    font-size: 236px; line-height: 236px;
  }
  .headline {
    position: absolute; left: 574px; top: 22px;
    color: var(--headline-gold);
    font-weight: 800; font-size: 66px; line-height: 70px;
    letter-spacing: 0.5px; white-space: nowrap;
  }
  .cuisine {
    position: absolute; left: 630px; top: 180px;
    color: var(--text-white);
    font-family: "Saira", sans-serif; font-weight: 700;
    font-size: 40px; line-height: 44px; letter-spacing: 4.5px; white-space: nowrap;
  }
  .brand-panel {
    position: absolute; left: 600px; top: 257px; width: 275px; height: 136px;
    background: var(--panel-white);
    display: flex; align-items: center; justify-content: center; gap: 10px;
  }
  .brand-name {
    color: var(--brand-orange);
    font-weight: 700; font-size: 25px; line-height: 25px;
    text-align: center;
  }
  .brand-dot {
    width: 22px; height: 22px; border-radius: 50%;
    background: var(--lime-dot); flex: none;
  }
  .location-panel {
    position: absolute; left: 875px; top: 257px; width: 325px; height: 136px;
    background: var(--panel-yellow);
  }
  .location-rule {
    position: absolute; left: 20px; top: 10px; width: 2px; height: 112px;
    background: var(--olive-green);
  }
  .location-text {
    position: absolute; left: 40px; top: 16px;
    color: var(--olive-green);
    font-weight: 700; font-size: 28px; line-height: 35px;
    white-space: nowrap;
  }
  .contact-line {
    position: absolute; left: 625px; top: 434px;
    color: var(--text-white);
    font-family: "Saira", sans-serif; white-space: nowrap;
    display: flex; align-items: baseline; gap: 12px;
  }
  .contact-web { font-weight: 500; font-size: 26px; }
  .contact-phone { font-weight: 500; font-size: 36px; letter-spacing: 0.5px; }
</style>
</head>
<body>
<main class="billboard">
  <div class="dining-photo" role="img" aria-label="Photo of a couple dining with a burger, fries and a glass of beer"></div>

  <div class="voted-badge">
    <p class="voted-words">Voted<br>Number<br>AGAIN!</p>
    <span class="voted-number">1</span>
  </div>

  <h1 class="headline">2 MILES<br>AHEAD ON RIGHT</h1>
  <p class="cuisine">CALIFORNIA CUISINE</p>

  <div class="brand-panel">
    <p class="brand-name">Marduvel's<br>Southwest<br>Bar &amp; Grill</p>
    <span class="brand-dot"></span>
  </div>

  <div class="location-panel">
    <span class="location-rule"></span>
    <p class="location-text">LOCATED IN<br>HISTORIC BRAMBLE<br>HOLLOW INN</p>
  </div>

  <p class="contact-line">
    <span class="contact-web">www.marduvel.com</span>
    <span class="contact-phone">555.317.0962</span>
  </p>
</main>
</body>
</html>
```